Overview of User Roles and their Functions

I need an overview of user roles and their functions. It should be presented on a A4 page to be shown during customer visits, but also put into our company presentation if possible.
I made a drawing with the information which needs to be mentioned (if it is not properly readable, please let me know)
The user roles are for our webportal Vantor-i Hub. To explain briefly: a producer can upload documents, and share them with distributors, who can use the same system to share documents with their customers. But a producer can also share documents directly with customers.
If you find a possibility to show these connections, may be with a document flying over to the right places, please try to implement this thought. Or additionally for the function: generate customer notification an email flying over to the distributor and customer. This could be flying over the top of the graph or underneath, or through it all, whatever works better without looking overloaded.
Producer and Distributor + are chargeable user accounts (you could add chargeable right underneath the title)
For the free distributor role I thought, this could all be slightly greyed out and have the Distributor + in more attractive colors. Producer and Customer can both be in attractive colors which stand out.
I tried to list the functions which are the same for different roles all on one line. May be you have a good idea about how not to let it look empty where there is no function mentioned?
Because I didn't have enough space, I didn't write docs properly as documents, or req.s as requests. Please choose a size where it is possible to write out the whole word.
as a background or generally, please use similar colors like on my website www.vantorihub.example . To make something stand out, you can also use different colors.
Please let me know if you have any additional questions. I am happy to answer them...
Target Market(s)
Pharmaceutical
Industry/Entity Type
Pharmaceutical
Font styles to use
Other font styles liked:
- if it is possible please use Raleway but if with Raleway the overview or readability is bad, use your own selected
Requirements
Must have
- clear overview of functions but if somehow possible, also show the connection the user roles can have with each other

```html
<!DOCTYPE html>
<html lang="en">
<head>
<meta charset="utf-8">
<title>Vantor-i Hub – User Roles and Functions</title>
<link rel="stylesheet" href="https://fonts.googleapis.com/css2?family=Raleway:ital,wght@0,400;0,500;1,400&display=swap">
<style>
  :root {
    --green: #7ab648;
    --blue: #2a72b8;
    --sky: #5bb6e1;
    --panel: #d6ecf5;
    --ink: #2b2b2b;
    --paper: #ffffff;
  }
  * { box-sizing: border-box; margin: 0; padding: 0; }
  html, body { width: 848px; height: 1200px; overflow: hidden; background: var(--paper); }
  body { font-family: 'Raleway', sans-serif; color: var(--ink); }
  .roles { position: relative; width: 848px; height: 1200px; }

  .role-tab {
    position: absolute; top: 81px; width: 198px; height: 66px;
    border-radius: 28px 28px 0 0;
    color: #fff; text-align: center;
    display: flex; flex-direction: column; justify-content: center; align-items: center;
  }
  .role-name { font-variant: small-caps; font-size: 26px; font-weight: 500; letter-spacing: 0.5px; line-height: 1; }
  .role-note { font-style: italic; font-size: 13px; margin-top: 2px; letter-spacing: 0.5px; }
  .tab-producer { left: 11px; background: var(--green); }
  .tab-distributor { left: 221px; background: var(--blue); }
  .tab-distributor-plus { left: 430px; background: var(--green); }
  .tab-customer { left: 641px; background: var(--sky); }

  .flow-arrow { position: absolute; width: 46px; height: 74px; }
  .flow-arrow.green { fill: var(--green); }
  .flow-arrow.blue { fill: var(--blue); }
  .flow-arrow.sky { fill: var(--sky); }

  .function-box {
    position: absolute; background: var(--panel);
    list-style: none; padding: 24px 14px 0 28px;
    font-size: 16px; line-height: 20px;
  }
  .function-box li { margin-bottom: 21px; }
  .function-box.tight { padding-left: 20px; }
</style>
</head>
<body>
<main class="roles">
  <!-- Role headers -->
  <div class="role-tab tab-producer"><span class="role-name">Producer</span></div>
  <div class="role-tab tab-distributor"><span class="role-name">Distributer</span><span class="role-note">(FREE)</span></div>
  <div class="role-tab tab-distributor-plus"><span class="role-name">Distributer +</span></div>
  <div class="role-tab tab-customer"><span class="role-name">Customer</span><span class="role-note">(FREE)</span></div>

  <!-- Arrows below headers -->
  <svg class="flow-arrow green" style="left:87px;top:167px" viewBox="0 0 46 74"><polygon points="16,0 30,0 30,44 46,44 23,74 0,44 16,44"/></svg>
  <svg class="flow-arrow blue" style="left:297px;top:167px" viewBox="0 0 46 74"><polygon points="16,0 30,0 30,44 46,44 23,74 0,44 16,44"/></svg>
  <svg class="flow-arrow green" style="left:506px;top:167px" viewBox="0 0 46 74"><polygon points="16,0 30,0 30,44 46,44 23,74 0,44 16,44"/></svg>
  <svg class="flow-arrow sky" style="left:717px;top:167px" viewBox="0 0 46 74"><polygon points="16,0 30,0 30,44 46,44 23,74 0,44 16,44"/></svg>

  <!-- Producer -->
  <ul class="function-box" style="left:14px;top:259px;width:193px;height:280px">
    <li>Upload<br>Documents</li>
    <li>Share</li>
    <li>Upload COAS</li>
    <li>Generate<br>Customer<br>Notifications</li>
  </ul>
  <svg class="flow-arrow green" style="left:87px;top:567px" viewBox="0 0 46 74"><polygon points="16,0 30,0 30,44 46,44 23,74 0,44 16,44"/></svg>
  <ul class="function-box tight" style="left:14px;top:661px;width:193px;height:433px">
    <li>Recieve Access<br>Requests</li>
    <li>Versioning System<br>(View Difference<br>Between DD/Ne<br>File)</li>
    <li>Expiry Notifications</li>
    <li>Reports</li>
    <li>Automated<br>Emailed Reports</li>
    <li>Set Stamps On<br>Documents</li>
  </ul>

  <!-- Distributor (free) -->
  <ul class="function-box tight" style="left:224px;top:259px;width:191px;height:137px">
    <li>Share</li>
    <li>Download<br>Documents</li>
  </ul>
  <svg class="flow-arrow blue" style="left:297px;top:425px" viewBox="0 0 46 74"><polygon points="16,0 30,0 30,44 46,44 23,74 0,44 16,44"/></svg>
  <ul class="function-box tight" style="left:224px;top:519px;width:191px;height:272px">
    <li>Receive<br>Notifications</li>
    <li>View Other Listed<br>Supplies</li>
    <li>Request Access</li>
    <li>Versioning System</li>
  </ul>

  <!-- Distributor + -->
  <ul class="function-box tight" style="left:435px;top:259px;width:189px;height:178px">
    <li>Upload Documents</li>
    <li>Share</li>
    <li>Download<br>Documents</li>
  </ul>
  <svg class="flow-arrow green" style="left:506px;top:459px" viewBox="0 0 46 74"><polygon points="16,0 30,0 30,44 46,44 23,74 0,44 16,44"/></svg>
  <ul class="function-box tight" style="left:435px;top:553px;width:189px;height:533px;padding-top:56px">
    <li>Generate Customer<br>Notifications</li>
    <li>Receive<br>Notifications</li>
    <li>View Other Used<br>Supplies</li>
    <li>Request Access</li>
    <li>Versioning System</li>
    <li>Expiry Notifications</li>
    <li>Reports</li>
    <li>Automated Email<br>Reports</li>
    <li>Set Stamps On</li>
  </ul>

  <!-- Customer (free) -->
  <ul class="function-box" style="left:648px;top:259px;width:187px;height:103px">
    <li>Download<br>Documents</li>
  </ul>
  <svg class="flow-arrow sky" style="left:717px;top:385px" viewBox="0 0 46 74"><polygon points="16,0 30,0 30,44 46,44 23,74 0,44 16,44"/></svg>
  <ul class="function-box" style="left:648px;top:472px;width:187px;height:278px">
    <li>Receive<br>Notifications</li>
    <li>View Other Used<br>Supplies</li>
    <li>Request Access</li>
    <li>Versioning System</li>
  </ul>
</main>
</body>
</html>
```